Fernhold Capital - Web Design

I have recently established a business called Fernhold Capital. The business is focused on providing property developers with project financing solutions. This is not a real estate website so please do not provide such pics or design. I provide financial solutions.

I have been in the financial markets for the past 20 years covering all asset classes from trading through to portfolio management, structuring and business development. The majority of this time was spent with building new business and expanding into new opportunities.

This is a start-up business so there isn't much content at this stage. Therefore, its all about first impressions. I want a design that portray confidence; and that I can deliver a workable solution. It must provide the perception of sophistication, innovation, yet simplistic so its not trying to deceive/hide something. Most importantly it must give the Client a sense of trust and reliability.

I would like to have the website portray my depth of experience in providing financing solutions and consultancy services in achieving the investment objectives. However, I would like to avoid looking like a one man band. I do have access to resources just not directly employed by the company.

Anyway, I hope this is enough to at least wet your appetite. I recently had a logo created on PixelGuild that should set the theme/style of the website

Project Deadline Extended
Reason: Increase time to allow web designer/developer more time to understand the style I am after.

All, Thank you for your current designs. I am based in Singapore, however, I am currently traveling today but will respond by later tonight or tomorrow. Owen

All, A general observation. Please do not include photos of houses, architectural drawings or images that portal construction or real estate. This implies I am either a property agent or in some way directly involve in selling property...very misleading. Remember, I am involved in provide financial solutions not selling property. Owen

All, Please avoid using numerous people within the site as it may represent that my business has a large number of staff when in fact its only me. However, I also don't want to look like a "one man band". So be balanced on using people - I am not sure I want people at all. Thanks Owen

Some designers are not reading the brief or previous messages. If you do more then once I will simply not comment and eliminate ask not to provide any more.

please stop using pictures and/or logos that imply - I manage their money - I protect their money - I grow their money - I offer homes loans - that I do house calls with individuals (i.e no couples shaking heads with a guy) - no house pictures or symbols i.e. it looks like a property website - I have a large organisation (i.e. team of people) If any design include the above I will eliminate it REMEMBER: I am providing innovative financial solutions - NOT asset/fund manager, bank manager or real estate manager thank you

All Please be creative and innovative with your pics. Also ensure you have the rights to use the pics. I have seen basic stock photos being used and again have not read by brief or previous comments. For instance, they use the words "sustainable growth" in google and click on images and you will see most of the images being used. these will be eliminated instantly and not asked to return.

Please, if you use the name of the Company as a Label or Statement can please ensure it remains in the same style as the Logo, i.e. all Caps Large with small.

All, I have decided that I don't want to have people in the main pic on the front page so please provide other inspirational pics. Thanks

guys I found a coffee advert whilst in Vietnam. I like the colour selection and thought it would be inspirational.i ahve added it yo my bried f

Real Estate

Coded - Design and coding required

```html
<!DOCTYPE html>
<html lang="en">
<head>
<meta charset="utf-8">
<title>Fernhold Capital</title>
<link href="https://fonts.googleapis.com/css2?family=Lato:wght@400;700;900&display=swap" rel="stylesheet">
<style>
:root{
  --gold:#c9ad2e;
  --gold-text:#b59a1f;
  --nav-text:#4a3c10;
  --black:#050505;
  --ink:#222;
  --body:#444;
  --white:#fff;
}
*{margin:0;padding:0;box-sizing:border-box}
html,body{width:853px;height:1200px;overflow:hidden;background:var(--white);font-family:'Lato',sans-serif;color:var(--body)}
.page{position:relative;width:853px;height:1200px}
.abs{position:absolute}

.topbar{left:0;top:0;width:853px;height:52px;background:var(--black);border-top:2px solid var(--gold)}
.brand{left:93px;top:12px;display:flex;align-items:center;gap:7px}
.brand-dot{width:22px;height:22px;border-radius:50%;background:var(--gold)}
.brand-name{font-weight:700;font-size:13px;letter-spacing:1.5px;color:var(--gold);text-transform:uppercase;line-height:1;white-space:nowrap}
.brand-name small{font-size:9px}
.callout{left:529px;top:18px;font-size:14.5px;font-weight:700;color:var(--gold)}
.social-top{left:689px;top:17px;display:flex;gap:2px}
.social-top span{width:24px;height:20px;background:var(--gold);border-radius:2px;display:flex;align-items:center;justify-content:center}

.nav{left:0;top:52px;width:853px;height:29px;background:var(--gold)}
.nav ul{list-style:none;position:absolute;left:89px;top:0;display:flex;height:29px;border-left:1px solid rgba(0,0,0,.18)}
.nav li{height:29px;display:flex;align-items:center;justify-content:center;font-size:9.6px;color:var(--nav-text);border-right:1px solid rgba(0,0,0,.18)}

.hero{left:0;top:81px;width:853px;height:361px;background:linear-gradient(180deg,#b9bfc2 0%,#8a8f90 30%,#5a5b58 60%,#2c2a26 100%)}

.welcome-mark{left:418px;top:470px;width:18px;height:18px;border-radius:50%;background:var(--gold)}
.welcome-title{left:0;top:508px;width:853px;text-align:center;font-size:19px;font-weight:700;color:var(--ink)}
.welcome-title em,.section-title em,.footer-title em{font-style:normal;color:var(--gold-text)}
.welcome-text{left:96px;top:534px;width:662px;text-align:center;font-size:8.6px;line-height:14.6px;color:#333}

.services{left:0;top:597px;width:853px;height:213px;background:linear-gradient(135deg,#6d5222 0%,#9b7a3c 35%,#7a5d2a 65%,#4f3a17 100%)}
.card{top:641px;width:212px;height:138px;background:var(--white);border:1px solid #d8d8d8;text-align:center}
.card h3{margin-top:43px;font-size:15.5px;font-weight:700;color:#333}
.card p{margin:8px auto 0;width:190px;font-size:8.6px;line-height:14.6px;color:#444}
.badge{top:608px;width:62px;height:62px;border-radius:50%;background:var(--white);border:1px solid #aaa;display:flex;align-items:center;justify-content:center}

.section-title{top:835px;font-size:18.5px;font-weight:700;color:var(--ink)}
.rule{top:862px;height:2px;background:var(--gold)}

.about-photo{left:89px;top:882px;width:97px;height:66px;background:linear-gradient(135deg,#d99a2a,#8a4a10)}
.about-side{left:196px;top:879px;width:107px;font-size:8.8px;line-height:14.6px;text-align:justify;color:#444}
.about-body{left:89px;top:953px;width:214px;font-size:8.8px;line-height:14.6px;text-align:justify;color:#444}

.news-item{left:320px;width:205px;height:50px}
.date{position:absolute;left:0;top:0;width:40px;height:38px;background:#e4e4e4;text-align:center}
.date b{display:block;height:13px;background:var(--gold);font-size:7.5px;line-height:13px;font-weight:400;color:#333}
.date span{font-size:17px;line-height:24px;font-weight:700;color:#333}
.news-item h4{position:absolute;left:49px;top:0;font-size:9px;font-weight:700;color:#222}
.news-item p{position:absolute;left:49px;top:13px;width:155px;font-size:7.8px;line-height:12px;color:#555}

.blog-photo{left:551px;width:97px;height:77px}
.blog-text{left:658px;width:108px}
.blog-text h4{font-size:8.8px;line-height:13.4px;font-weight:700;color:#222}
.blog-text .when{font-size:8px;color:var(--gold-text);margin-top:2px}
.blog-text p{font-size:7.8px;line-height:13.4px;color:#555;margin-top:1px}

.footer{left:0;top:1081px;width:853px;height:119px;background:var(--black)}
.footer-brand{left:100px;top:1096px;width:140px;text-align:center}
.footer-brand .brand-dot{display:block;margin:0 auto 7px}
.footer-brand .brand-name{font-size:11px;display:block}
.copy{left:110px;top:1158px;width:120px;text-align:center;font-size:8.8px;line-height:14px;color:var(--white)}
.footer-title{top:1089px;font-size:16px;font-weight:400;color:var(--white)}
.links{left:315px;top:1112px;list-style:none;font-size:8.8px;line-height:15.4px;color:var(--white)}
.links li::before{content:"»";margin-right:6px}
.contact-row{left:452px;font-size:8.8px;color:var(--white);display:flex;gap:9px;line-height:18px}
.contact-row svg{margin-top:4px;flex:none}
.social-foot{left:633px;top:1128px;display:flex;gap:8px}
.social-foot span{width:30px;height:26px;background:var(--gold);display:flex;align-items:center;justify-content:center}
</style>
</head>
<body>
<div class="page">

  <header class="abs topbar"></header>
  <div class="abs brand"><span class="brand-dot"></span><span class="brand-name">F<small>ERNHOLD</small> C<small>APITAL</small></span></div>
  <div class="abs callout">Call on : (555) 310 4729</div>
  <div class="abs social-top" aria-label="Social links">
    <span><svg width="11" height="10" viewBox="0 0 11 10"><path d="M1 1h9v6H5L2 9V7H1z" fill="#fff"/></svg></span>
    <span><svg width="11" height="10" viewBox="0 0 11 10"><circle cx="2" cy="5" r="1.6" fill="#fff"/><circle cx="9" cy="1.8" r="1.6" fill="#fff"/><circle cx="9" cy="8.2" r="1.6" fill="#fff"/><path d="M2 5L9 1.8M2 5L9 8.2" stroke="#fff"/></svg></span>
    <span><svg width="11" height="9" viewBox="0 0 11 9"><rect x=".5" y=".5" width="10" height="8" fill="none" stroke="#fff"/><polyline points=".5,.5 5.5,5 10.5,.5" fill="none" stroke="#fff"/></svg></span>
  </div>

  <nav class="abs nav">
    <ul>
      <li style="width:69px">Home</li>
      <li style="width:81px">About Us</li>
      <li style="width:136px">Portfolio Management</li>
      <li style="width:91px">Structuring</li>
      <li style="width:134px">Business Devlopment</li>
      <li style="width:72px">Service</li>
      <li style="width:92px">Contact Us</li>
    </ul>
  </nav>

  <div class="abs hero" role="img" aria-label="Aerial photograph of a dense city skyline of skyscrapers"></div>

  <span class="abs welcome-mark"></span>
  <h1 class="abs welcome-title">WELCOME <em>FERNHOLD CAPITAL</em></h1>
  <p class="abs welcome-text">It is a long established fact that a reader will be distracted by the readable content of a page when looking at its layout. The point of using Lorem Ipsum is that it has a more-or-less normal distribution of letters, as opposed to using 'Content here, content here', making it look like readable English. Many desktop publishing packages and web page editors now use Lorem Ipsum as their default model text,</p>

  <div class="abs services" role="img" aria-label="Warm close-up photograph of coins and banknotes"></div>

  <div class="abs card" style="left:89px"><h3>Portfolio Management</h3><p>It is a long established fact that a reader will be distracted by the readable content of a page when looking at its layout.</p></div>
  <div class="abs card" style="left:321px"><h3>Structuring</h3><p>It is a long established fact that a reader will be distracted by the readable content of a page when looking at its layout.</p></div>
  <div class="abs card" style="left:552px"><h3>Business Devlopment</h3><p>It is a long established fact that a reader will be distracted by the readable content of a page when looking at its layout.</p></div>

  <div class="abs badge" style="left:164px">
    <svg width="30" height="26" viewBox="0 0 30 26"><rect x="10" y="1" width="10" height="5" fill="none" stroke="#c9ad2e" stroke-width="2"/><rect x="1" y="6" width="28" height="19" fill="#c9ad2e"/><rect x="1" y="13" width="28" height="2" fill="#fff"/><rect x="12" y="11" width="6" height="6" fill="#fff"/></svg>
  </div>
  <div class="abs badge" style="left:396px">
    <svg width="38" height="24" viewBox="0 0 38 24" fill="#c9ad2e" stroke="#c9ad2e"><circle cx="19" cy="4" r="3"/><line x1="19" y1="4" x2="4" y2="20"/><line x1="19" y1="4" x2="11" y2="20"/><line x1="19" y1="4" x2="19" y2="20"/><line x1="19" y1="4" x2="27" y2="20"/><line x1="19" y1="4" x2="34" y2="20"/><circle cx="4" cy="20" r="2.5"/><circle cx="11" cy="20" r="2.5"/><circle cx="19" cy="20" r="2.5"/><circle cx="27" cy="20" r="2.5"/><circle cx="34" cy="20" r="2.5"/></svg>
  </div>
  <div class="abs badge" style="left:627px">
    <svg width="32" height="30" viewBox="0 0 32 30" fill="#c9ad2e"><rect x="1" y="1" width="2" height="28"/><rect x="1" y="27" width="30" height="2"/><rect x="6" y="18" width="4" height="8"/><rect x="12" y="14" width="4" height="12"/><rect x="18" y="16" width="4" height="10"/><rect x="24" y="9" width="4" height="17"/><polyline points="6,14 13,8 19,11 29,3" fill="none" stroke="#c9ad2e" stroke-width="2"/></svg>
  </div>

  <h2 class="abs section-title" style="left:91px">ABOUT US</h2>
  <span class="abs rule" style="left:89px;width:93px"></span>
  <h2 class="abs section-title" style="left:319px">LATEST <em>NEWS</em></h2>
  <span class="abs rule" style="left:319px;width:121px"></span>
  <h2 class="abs section-title" style="left:551px">LATEST <em>BLOG</em></h2>
  <span class="abs rule" style="left:551px;width:119px"></span>

  <div class="abs about-photo" role="img" aria-label="Photograph of stacked gold coins, banknotes and a pocket watch"></div>
  <p class="abs about-side">Lorem Ipsum is simply dummy text of the printing and typesetting industry. Lorem Ipsum has been the industry'sstandard dummy</p>
  <p class="abs about-body">Lorem Ipsum is simply dummy text of the printing and typesetting industry. Lorem Ipsum has been the indus-try's standard dummy text ever since the 1500s, when an unknown printer took a galley of type and scrambled it to make a type specimen book. It has sur-vived not only five centuries, but also the leap into</p>

  <article class="abs news-item" style="top:882px"><div class="date"><b>March</b><span>15</span></div><h4>Lorem Ipsum is simply dummy text</h4><p>Lorem Ipsum is simply dummy text of the printing and typesetting industry. Lorem Ipsum has</p></article>
  <article class="abs news-item" style="top:944px"><div class="date"><b>March</b><span>15</span></div><h4>Lorem Ipsum is simply dummy text</h4><p>Lorem Ipsum is simply dummy text of the printing and typesetting industry. Lorem Ipsum has</p></article>
  <article class="abs news-item" style="top:1004px"><div class="date"><b>March</b><span>15</span></div><h4>Lorem Ipsum is simply dummy text</h4><p>Lorem Ipsum is simply dummy text of the printing and typesetting industry. Lorem Ipsum has</p></article>

  <div class="abs blog-photo" style="top:880px;background:linear-gradient(135deg,#f0ede6,#c9b27a 60%,#8a7640)" role="img" aria-label="Photograph of a hand stacking coins in rising columns"></div>
  <div class="abs blog-text" style="top:877px"><h4>Lorem Ipsum is simply du mmy text ofthe printing</h4><div class="when">20 March 2014</div><p>There are many variations of passages of Lorem Ipsum available, but the majority</p></div>
  <div class="abs blog-photo" style="top:973px;background:linear-gradient(135deg,#dcd6cc,#6b5a44 55%,#2e2418)" role="img" aria-label="Photograph of cupped hands holding soil with a green seedling"></div>
  <div class="abs blog-text" style="top:970px"><h4>Lorem Ipsum is simply du mmy text ofthe printing</h4><div class="when">20 March 2014</div><p>There are many variations of passages of Lorem Ipsum available, but the majority</p></div>

  <footer class="abs footer"></footer>
  <div class="abs footer-brand"><span class="brand-dot"></span><span class="brand-name">F<small>ERNHOLD</small> C<small>APITAL</small></span></div>
  <p class="abs copy">All © Copy Right Of Fernholdcapital is reserd</p>

  <h3 class="abs footer-title" style="left:302px">Quick <em>Links</em></h3>
  <ul class="abs links"><li>Home</li><li>About Us</li><li>Service</li><li>Solutions</li><li>Contact Us</li></ul>

  <h3 class="abs footer-title" style="left:464px">Contact <em>Us</em></h3>
  <div class="abs contact-row" style="top:1112px"><svg width="7" height="10" viewBox="0 0 7 10"><path d="M3.5 0A3.5 3.5 0 0 0 0 3.5C0 6 3.5 10 3.5 10S7 6 7 3.5A3.5 3.5 0 0 0 3.5 0z" fill="#fff"/><circle cx="3.5" cy="3.5" r="1.3" fill="#050505"/></svg><span>48 Harlow Quay Suite 9<br>Marlowe 40217</span></div>
  <div class="abs contact-row" style="top:1152px"><svg width="9" height="9" viewBox="0 0 9 9"><path d="M2 0L3.5 2.5 2.5 3.5C3 5 4 6 5.5 6.5L6.5 5.5 9 7 8 9C4 9 0 5 0 1z" fill="#fff"/></svg><span>555 201 6634</span></div>
  <div class="abs contact-row" style="top:1172px"><svg width="10" height="8" viewBox="0 0 10 8"><rect width="10" height="8" fill="#fff"/><polyline points="0,0 5,4.5 10,0" fill="none" stroke="#050505"/></svg><span>hello@fernhold.co</span></div>

  <h3 class="abs footer-title" style="left:646px">Follow <em>Us</em></h3>
  <div class="abs social-foot" aria-label="Social links">
    <span><svg width="14" height="13" viewBox="0 0 14 13"><path d="M1 1h12v8H6L2 12V9H1z" fill="#050505"/></svg></span>
    <span><svg width="14" height="13" viewBox="0 0 14 13"><circle cx="3" cy="6.5" r="2.2" fill="#050505"/><circle cx="11" cy="2.5" r="2.2" fill="#050505"/><circle cx="11" cy="10.5" r="2.2" fill="#050505"/><path d="M3 6.5L11 2.5M3 6.5L11 10.5" stroke="#050505" stroke-width="1.3"/></svg></span>
    <span><svg width="14" height="11" viewBox="0 0 14 11"><rect x=".7" y=".7" width="12.6" height="9.6" fill="none" stroke="#050505" stroke-width="1.4"/><polyline points=".7,.7 7,6 13.3,.7" fill="none" stroke="#050505" stroke-width="1.4"/></svg></span>
  </div>

</div>
</body>
</html>
```